Fast Money - Simple Book Cover Design

Hello,

I am in need of a cover for my new book. The Book Title Is

"Standing Growth - Keys to Glowing Customer Ratings That Fill The Calendar and Draw Fresh Clients Through Every Entrance!"

Author: Mentor Dale Orsworth

What I want: This is a book for businesses on improving their online reputation. I want to have 5 Stars on the cover. You can look at this quarvex search for ideas of what I am meaning.....

(copy and paste)

http://www.quarvex-find.example/search?q=5+star+online+reviews&mode=images&ref=kx7Lp2QwZt9 (copy and paste)

I am open to different color schemes for the book. I am partial to dark blues if you make it look good. Here is another book that I really like the cover of....

http://www.brindlemart.example/Clipwave-Tactics-Earning-Promotion-ebook/item/Z93KT4WQPX

I want the cover BOLD and to STAND OUT.

I am looking for a design to help establish me as an authority for online reputation marketing. This book will be both in Pagely format and be used in print as well.

I am open to questions....

Thanks!

Dale

Reason: I don't believe we have received the right designs. I am going to give everyone more time...

Reason: Hi everyone, I had some stuff come up and was not able to be involved in this project. I am extending because we have not seen the exact thing we want and need time to work with designers to get it right. Thanks Dale

Reason: I am currently traveling and can't wrap this up until I get back.

Target Market(s)

Business Owners

Industry/Entity Type

Business

Requirements
Must have
• Title and Subtitle

Author Name

5 Stars Images....
Nice to have
• Creativity

Bold and stand out

Professional

Should not have
• thin text, small to read text, lame graphics,

```html
<!DOCTYPE html>
<html lang="en">
<head>
<meta charset="utf-8">
<title>Standing Growth – Book Cover</title>
<link rel="stylesheet" href="https://fonts.googleapis.com/css2?family=Arimo:wght@400;700&family=Open+Sans:wght@400;600;700;800&display=swap">
<style>
  :root {
    --cyan: #5cf6fa;
    --cyan-feature: #4fe4ee;
    --vignette: #0b2c30;
    --white: #ffffff;
    --ink: #050808;
    --bevel: #7f8b8e;
    --bevel-light: #c3ccce;
    --star-light: #d4fcff;
    --star-mid: #62e8f2;
  }
  html, body {
    margin: 0;
    padding: 0;
    width: 797px;
    height: 1200px;
    overflow: hidden;
    background: var(--vignette);
  }
  .cover {
    position: relative;
    width: 797px;
    height: 1200px;
    overflow: hidden;
    background: var(--cyan);
    box-shadow: inset 0 0 70px 24px var(--vignette), inset 0 0 140px 30px rgba(11,44,48,0.55);
    font-family: "Open Sans", "Segoe UI", sans-serif;
  }
  .title {
    position: absolute;
    left: 0;
    width: 797px;
    margin: 0;
    text-align: center;
    font-family: "Arimo", Arial, sans-serif;
    font-weight: 700;
    font-size: 110px;
    line-height: 1;
    color: var(--white);
    -webkit-text-stroke: 2px var(--bevel);
    text-shadow: 2px 2px 0 var(--bevel-light), 4px 4px 0 var(--bevel), 6px 8px 8px rgba(0,0,0,0.35);
  }
  .title-line-1 { top: 46px; }
  .title-line-2 { top: 168px; }

  .tagline-lead {
    position: absolute;
    left: 28px;
    top: 398px;
    font-weight: 600;
    font-size: 50px;
    letter-spacing: -1.5px;
    color: var(--white);
    text-shadow: 1px 2px 2px rgba(0,0,0,0.25);
  }
  .tagline-feature {
    position: absolute;
    left: 328px;
    top: 318px;
    font-weight: 700;
    font-size: 104px;
    letter-spacing: -4px;
    color: var(--cyan-feature);
    text-shadow: 1px 1px 0 #a8fbff, 3px 5px 5px rgba(0,40,45,0.6);
  }
  .tagline-tail {
    position: absolute;
    left: 328px;
    top: 456px;
    font-weight: 600;
    font-size: 50px;
    letter-spacing: -1.5px;
    color: var(--white);
  }
  .promise {
    position: absolute;
    left: 44px;
    top: 586px;
    margin: 0;
    font-weight: 800;
    font-size: 55px;
    line-height: 60px;
    letter-spacing: -2.5px;
    color: var(--ink);
  }
  .promise .highlight { color: var(--white); font-weight: 700; }

  .author-band {
    position: absolute;
    left: 0;
    top: 896px;
    width: 797px;
    height: 164px;
    background: var(--ink);
  }
  .author-name {
    position: absolute;
    right: 22px;
    bottom: 14px;
    margin: 0;
    font-weight: 400;
    font-size: 52px;
    letter-spacing: 1px;
    color: var(--white);
  }
  .rating-stars {
    position: absolute;
    left: 0;
    top: 800px;
    width: 797px;
    height: 160px;
  }
</style>
</head>
<body>
  <main class="cover">
    <h1 class="title title-line-1">STANDING</h1>
    <p class="title title-line-2">GROWTH</p>

    <span class="tagline-lead">Keys to</span>
    <span class="tagline-feature">Glowing</span>
    <span class="tagline-tail">Customer Ratings</span>

    <p class="promise">That Fill The <span class="highlight">CALENDAR</span><br>and Draw <span class="highlight">Fresh Clients</span><br>Through Every Entrance</p>

    <div class="author-band">
      <p class="author-name">MENTOR Dale Orsworth</p>
    </div>

    <svg class="rating-stars" viewBox="0 0 797 160" role="img" aria-label="Five stars">
      <defs>
        <radialGradient id="star-fill" cx="50%" cy="40%" r="60%">
          <stop offset="0%" stop-color="var(--star-light)"/>
          <stop offset="100%" stop-color="var(--star-mid)"/>
        </radialGradient>
        <filter id="star-shadow" x="-30%" y="-30%" width="170%" height="170%">
          <feDropShadow dx="5" dy="7" stdDeviation="5" flood-color="#000" flood-opacity="0.5"/>
        </filter>
        <polygon id="star" points="0,-66 15.5,-21.4 62.8,-20.4 25.1,8.2 38.8,53.4 0,26.4 -38.8,53.4 -25.1,8.2 -62.8,-20.4 -15.5,-21.4"/>
      </defs>
      <g fill="url(#star-fill)" stroke="#e9feff" stroke-width="1.5" filter="url(#star-shadow)">
        <use href="#star" x="138" y="88"/>
        <use href="#star" x="266" y="88"/>
        <use href="#star" x="393" y="88"/>
        <use href="#star" x="521" y="88"/>
        <use href="#star" x="648" y="88"/>
      </g>
    </svg>
  </main>
</body>
</html>
```